Boutique Wealth management firm needs a new business card design

I want to update my business card design to be more consistent with the look and feel of my website (www.corvalen-capital.example). I would like to incorporate an ivory parchment background and am open to switching from the current "portrait" layout to a more traditional "landscape" orientation. The final design should convey stability and exclusivity and I want something in PDF format that is ready to send to the printer
Updates

Thank you all for taking the time to submit your designs for my project. I've made my decision and picked the design I like best. Thanks again!

Industry/Entity Type

Business

```html
<!DOCTYPE html>
<html lang="en">
<head>
<meta charset="utf-8">
<title>Corvalen Capital Advisory – Business Card</title>
<link rel="stylesheet" href="https://fonts.googleapis.com/css2?family=Libre+Baskerville:wght@400;700&family=Open+Sans:wght@400;700&display=swap">
<style>
  :root {
    --backdrop: #2a1416;
    --ivory-light: #fbf3d6;
    --ivory: #f2e4b4;
    --ivory-deep: #e6d29a;
    --maroon: #6b2437;
    --ink: #141414;
    --band-text: #f6ecd6;
  }
  * { box-sizing: border-box; margin: 0; padding: 0; }
  html, body {
    width: 1200px; height: 800px; overflow: hidden;
    background: var(--backdrop);
  }
  .card {
    position: absolute; left: 150px; top: 143px;
    width: 900px; height: 514px;
    background:
      radial-gradient(ellipse at 30% 30%, var(--ivory-light) 0%, transparent 55%),
      radial-gradient(ellipse at 75% 65%, var(--ivory-light) 0%, transparent 50%),
      linear-gradient(135deg, var(--ivory) 0%, var(--ivory-deep) 100%);
    overflow: hidden;
  }
  .brand {
    position: absolute; left: 58px; top: 60px;
    font-family: "Libre Baskerville", serif; font-weight: 700;
    line-height: 1;
  }
  .brand__name { display: block; font-size: 66px; letter-spacing: 1px; color: var(--maroon); }
  .brand__sub { display: block; font-size: 30px; margin-top: 4px; text-align: right; color: var(--ink); }
  .advisor {
    position: absolute; right: 110px; top: 170px; text-align: right;
    font-family: "Open Sans", sans-serif; line-height: 1.2;
  }
  .advisor__name { font-size: 25px; font-weight: 700; color: var(--maroon); }
  .advisor__name sup { font-size: 12px; }
  .advisor__title { font-size: 13px; font-weight: 700; color: var(--ink); }
  .details {
    position: absolute; left: 60px; top: 246px;
    font-family: "Open Sans", sans-serif; font-size: 21px; color: var(--ink);
    line-height: 1.3;
  }
  .contact { list-style: none; }
  .contact li { display: flex; align-items: flex-start; gap: 10px; }
  .contact li + li { margin-top: 2px; }
  .contact .gap { margin-top: 12px; }
  .contact svg { width: 18px; height: 18px; margin-top: 6px; flex: none; fill: var(--maroon); }
  .license { margin-top: 12px; padding-left: 28px; font-size: 20px; }
  .rule {
    position: absolute; left: 0; right: 0; bottom: 60px; height: 6px; background: var(--ink);
  }
  .tagline {
    position: absolute; left: 0; right: 0; bottom: 0; height: 60px;
    background: var(--maroon); color: var(--band-text);
    font-family: "Libre Baskerville", serif; font-size: 21px;
    letter-spacing: 14px; display: flex; align-items: center; justify-content: center;
  }
</style>
</head>
<body>
  <section class="card">
    <div class="brand">
      <span class="brand__name">CORVALEN</span>
      <span class="brand__sub">Capital Advisory</span>
    </div>

    <div class="advisor">
      <div class="advisor__name">Daniel Ashford, CFP<sup>®</sup></div>
      <div class="advisor__title">Principal</div>
    </div>

    <div class="details">
      <ul class="contact">
        <li>
          <svg viewBox="0 0 24 24" aria-hidden="true"><path d="M6.6 10.8a15 15 0 0 0 6.6 6.6l2.2-2.2c.3-.3.7-.4 1-.2 1.1.4 2.3.6 3.6.6.6 0 1 .4 1 1V20c0 .6-.4 1-1 1A17 17 0 0 1 3 4c0-.6.4-1 1-1h3.5c.6 0 1 .4 1 1 0 1.3.2 2.5.6 3.6.1.3 0 .7-.2 1z"/></svg>
          925-555-0148
        </li>
        <li>
          <svg viewBox="0 0 24 24" aria-hidden="true"><path d="M2 5h20v14H2zm2 2v.5l8 5 8-5V7zm0 2.8V17h16V9.8l-8 5z"/></svg>
          dan@corvalen-capital.example
        </li>
        <li>
          <svg viewBox="0 0 24 24" aria-hidden="true"><path d="M12 2a10 10 0 1 0 0 20 10 10 0 0 0 0-20zm6.9 6h-2.9a15 15 0 0 0-1.3-3.6A8 8 0 0 1 18.9 8zM12 4a13 13 0 0 1 1.9 4h-3.8A13 13 0 0 1 12 4zM4.3 14a8 8 0 0 1 0-4h3.4a16 16 0 0 0 0 4zm.8 2h2.9a15 15 0 0 0 1.3 3.6A8 8 0 0 1 5.1 16zM8 8H5.1a8 8 0 0 1 4.2-3.6A15 15 0 0 0 8 8zm4 12a13 13 0 0 1-1.9-4h3.8A13 13 0 0 1 12 20zm2.3-6H9.7a14 14 0 0 1 0-4h4.6a14 14 0 0 1 0 4zm.4 5.6A15 15 0 0 0 16 16h2.9a8 8 0 0 1-4.2 3.6zm1.6-5.6a16 16 0 0 0 0-4h3.4a8 8 0 0 1 0 4z"/></svg>
          www.corvalen-capital.example
        </li>
        <li class="gap">
          <svg viewBox="0 0 24 24" aria-hidden="true"><path d="M12 3 2 12h3v8h5v-6h4v6h5v-8h3z"/></svg>
          <span>2870 Orchard Ln #212<br>Danville, CA 94526</span>
        </li>
      </ul>
      <p class="license">CA Insurance License #0K71863</p>
    </div>

    <div class="rule"></div>
    <div class="tagline">Guiding your Goals and Future</div>
  </section>
</body>
</html>
```